International Parcel Forwarder needs website redesign and logo

We need an updated website design to make our existing site look more modern, global and trustworthy. Current site
www.parvento.com -- we do not want to rebuild headers or at this point do copyright we are simply looking to make the site pop:)
The service we provide is for shoppers living outside the USA looking to shop here and save money on shipping or get access to stores that won't ship internationally or accept international payment.
Target Market(s)
Online shoppers living outside the USA
Industry/Entity Type
Shipping
Logo Text
US shopping, global shipping
Coding
Coded - Design and coding required
Number of Pages Required
5+ page
Font styles to use

```html
<!DOCTYPE html>
<html lang="en">
<head>
<meta charset="utf-8">
<title>Parvento – International Parcel Forwarder</title>
<link href="https://fonts.googleapis.com/css2?family=Lato:ital,wght@0,400;0,700;0,900;1,400&family=Open+Sans:wght@400;600&display=swap" rel="stylesheet">
<style>
:root{
  --green:#27ae6b;
  --navy:#174a8b;
  --navy-dark:#123d75;
  --ink:#222;
  --body:#555;
  --muted:#777;
  --pale:#f1f5fa;
  --line:#d9d9d9;
  --white:#fff;
}
*{box-sizing:border-box;margin:0;padding:0}
html,body{width:1200px;height:2442px;overflow:hidden;background:var(--white)}
body{position:relative;font-family:"Open Sans",Arial,sans-serif;color:var(--body)}
.abs{position:absolute}
a{color:inherit;text-decoration:none}

/* hero */
.hero{left:0;top:0;width:1200px;height:525px;overflow:hidden}
.hero-photo{position:absolute;inset:0;background:linear-gradient(180deg,#8ea2b8 0%,#a9b9c9 25%,#6f7f86 48%,#3e5a3a 62%,#35566e 78%,#2a4a63 100%)}
.hero-shade{position:absolute;inset:0;background:rgba(10,25,45,.25)}
.brand{left:98px;top:36px;display:flex;align-items:center;gap:10px;font-family:"Lato",sans-serif;font-weight:900;font-size:34px;color:var(--white)}
.brand-mark{width:26px;height:26px;background:var(--white)}
.topbar{right:98px;top:14px;display:flex;align-items:center;gap:22px;font-family:"Lato",sans-serif;font-size:16px;color:var(--white)}
.topbar .contact{display:flex;align-items:center;gap:10px}
.ico-round{width:30px;height:30px;border-radius:50%;background:var(--white);display:flex;align-items:center;justify-content:center}
.btn-pill{height:34px;border-radius:17px;padding:0 16px;display:flex;align-items:center;gap:7px;font-size:13px;font-weight:700;letter-spacing:.5px}
.btn-login{border:2px solid var(--white)}
.btn-signup{background:var(--green);border:2px solid var(--white)}
.nav{right:98px;top:66px;display:flex;gap:30px;align-items:center;font-family:"Lato",sans-serif;font-size:16px;color:var(--white)}
.hero-title{left:0;width:1200px;top:174px;text-align:center;font-family:"Lato",sans-serif;font-weight:700;font-size:46px;color:var(--white);text-shadow:0 2px 6px rgba(0,0,0,.35)}
.hero-sub{left:0;width:1200px;top:238px;text-align:center;font-family:"Lato",sans-serif;font-size:27px;color:var(--white)}
.hero-btn{left:491px;top:295px;width:218px;height:42px;border:2px solid var(--white);border-radius:21px;display:flex;align-items:center;justify-content:center;font-family:"Lato",sans-serif;font-weight:700;font-size:15px;color:var(--white)}
.dots{left:567px;top:467px;display:flex;gap:6px}
.dots span{width:14px;height:14px;border-radius:50%;border:2px solid var(--white)}
.dots span.on{background:var(--white)}

/* welcome */
.section-title{font-family:"Lato",sans-serif;font-weight:700;color:var(--ink)}
.welcome-title{left:98px;top:576px;font-size:28px}
.welcome-text{left:98px;top:632px;width:480px;font-size:12.5px;line-height:24px;color:var(--body)}
.welcome-text p+p{margin-top:24px}
.btn-outline{border:2px solid #bfbfbf;color:var(--green)}
.btn-solid{background:var(--green);color:var(--white)}
.btn-rect{height:42px;border-radius:21px;display:flex;align-items:center;justify-content:center;font-family:"Lato",sans-serif;font-weight:700;font-size:14px;letter-spacing:.5px}
.btn-learn{left:98px;top:832px;width:166px}
.btn-join{left:278px;top:832px;width:166px}
.video{left:606px;top:581px;width:496px;height:300px;border:1px solid var(--line);padding:5px;background:var(--white);box-shadow:0 1px 4px rgba(0,0,0,.15)}
.video-photo{width:100%;height:100%;background:linear-gradient(110deg,#9aa6b0 0%,#c9b38e 45%,#b48657 75%,#8a6a4c 100%);position:relative}
.play{position:absolute;left:50%;top:50%;width:64px;height:64px;margin:-32px 0 0 -32px;border-radius:50%;background:rgba(0,0,0,.75);border:2px solid rgba(255,255,255,.8);display:flex;align-items:center;justify-content:center}

/* how it works */
.how{left:0;top:941px;width:1200px;height:423px;background:var(--pale)}
.how-title{left:0;width:1200px;top:996px;text-align:center;font-size:26px}
.step-circle{width:146px;height:146px;border-radius:50%;border:2px solid var(--navy);background:var(--white);display:flex;align-items:center;justify-content:center}
.step-num{width:36px;height:36px;border-radius:50%;background:var(--navy);color:var(--white);font-family:"Lato",sans-serif;font-weight:700;font-size:17px;display:flex;align-items:center;justify-content:center}
.step-caption{width:240px;text-align:center;font-family:"Lato",sans-serif;font-size:15px;line-height:26px;color:#333}

/* why */
.why-photo{left:0;top:1364px;width:602px;height:461px;background:linear-gradient(120deg,#5d4a38 0%,#8a7156 35%,#b79a78 60%,#6e5a46 100%)}
.why-panel{left:602px;top:1364px;width:598px;height:461px;background:var(--navy)}
.why-title{left:653px;top:1404px;font-family:"Lato",sans-serif;font-weight:700;font-size:26px;color:var(--white)}
.why-sub{left:653px;top:1453px;font-size:12.5px;color:var(--white)}
.feature{display:flex;align-items:center;gap:14px;color:var(--white)}
.feature-icon{width:68px;height:68px;border-radius:50%;border:2px solid var(--white);display:flex;align-items:center;justify-content:center}
.feature-name{font-family:"Lato",sans-serif;font-weight:700;font-size:16px}
.feature-note{font-family:"Lato",sans-serif;font-style:italic;font-size:12.5px;margin-top:4px}
.why-btn{left:653px;top:1737px;width:166px;height:41px;border:2px solid var(--white);border-radius:21px;display:flex;align-items:center;justify-content:center;font-family:"Lato",sans-serif;font-weight:700;font-size:13px;color:var(--white)}

/* partners */
.partners-title{left:0;width:1200px;top:1880px;text-align:center;font-size:26px}
.partner{width:187px;height:79px;border:2px solid #cfcfcf;display:flex;align-items:center;justify-content:center;background:var(--white)}
.partner-shape{width:110px;height:26px;border-radius:13px;background:#dfe3e8}

/* footer */
.footer-rule{left:0;top:2096px;width:1200px;height:4px;background:var(--green)}
.footer-col{top:2152px}
.footer-col h4{font-family:"Lato",sans-serif;font-weight:700;font-size:17px;color:var(--ink);margin-bottom:12px}
.footer-col li{list-style:none;font-size:12px;line-height:26.5px;color:var(--body)}
.col-sep{top:2140px;width:1px;height:210px;background:#e3e3e3}
.sub-note{font-size:12px;color:var(--body);margin-bottom:14px}
.sub-form{display:flex}
.sub-input{width:230px;height:35px;border:1px solid #cfcfcf;font-size:12px;color:var(--muted);padding:0 12px;display:flex;align-items:center}
.sub-btn{width:92px;height:35px;background:var(--green);color:var(--white);font-family:"Lato",sans-serif;font-weight:700;font-size:12.5px;display:flex;align-items:center;justify-content:center}
.social{display:flex;gap:10px;margin-top:12px}
.social span{width:32px;height:32px;border-radius:50%}
.footer-bottom-rule{left:98px;top:2374px;width:1004px;height:1px;background:#e3e3e3}
.copyright{left:0;width:1200px;top:2400px;text-align:center;font-size:11.5px;color:#444}
</style>
</head>
<body>

<section class="abs hero">
  <div class="hero-photo" role="img" aria-label="City skyline beside a river under a cloudy sky"></div>
  <div class="hero-shade"></div>
</section>

<div class="abs brand"><span class="brand-mark"></span>Parvento</div>

<div class="abs topbar">
  <div class="contact">
    <span class="ico-round"><svg width="16" height="16" viewBox="0 0 24 24"><path fill="#333" d="M6.6 10.8a15 15 0 0 0 6.6 6.6l2.2-2.2c.3-.3.7-.4 1-.2 1.1.4 2.3.6 3.6.6.6 0 1 .4 1 1V20c0 .6-.4 1-1 1A17 17 0 0 1 3 4c0-.6.4-1 1-1h3.5c.6 0 1 .4 1 1 0 1.3.2 2.5.6 3.6.1.3 0 .7-.2 1z"/></svg></span>
    1-555-014-2290
  </div>
  <div class="contact">
    <span class="ico-round"><svg width="16" height="16" viewBox="0 0 24 24"><path fill="#333" d="M3 5h18v14H3z"/><path fill="none" stroke="#fff" stroke-width="2" d="M3 6l9 7 9-7"/></svg></span>
    support@parvento.com
  </div>
  <div style="display:flex;gap:6px">
    <a class="btn-pill btn-login"><svg width="11" height="13" viewBox="0 0 12 14"><rect x="1" y="6" width="10" height="8" rx="1" fill="#fff"/><path d="M3 6V4a3 3 0 0 1 6 0v2" stroke="#fff" stroke-width="1.8" fill="none"/></svg>LOGIN</a>
    <a class="btn-pill btn-signup"><svg width="12" height="12" viewBox="0 0 24 24"><path fill="#fff" d="M3 17.2V21h3.8L18 9.8 14.2 6zM20.7 7a1 1 0 0 0 0-1.4l-2.3-2.3a1 1 0 0 0-1.4 0l-1.8 1.8 3.8 3.8z"/></svg>SIGN UP</a>
  </div>
</div>

<nav class="abs nav">
  <a>Shipping Calculator</a><a>How It Works</a><a>Parvento Pricing</a><a>Blog</a><a>Contact Us</a>
  <svg width="16" height="16" viewBox="0 0 24 24"><circle cx="10" cy="10" r="7" stroke="#fff" stroke-width="3" fill="none"/><path d="M15 15l6 6" stroke="#fff" stroke-width="3"/></svg>
</nav>

<h1 class="abs hero-title">Shop at any U.S. retailer. Ship anywhere.</h1>
<p class="abs hero-sub">We are an international parcel forwarder</p>
<a class="abs hero-btn">GET MORE INFO &gt;&gt;</a>
<div class="abs dots"><span class="on"></span><span></span><span></span><span></span></div>

<!-- welcome -->
<h2 class="abs section-title welcome-title">Welcome to Parvento</h2>
<div class="abs welcome-text">
  <p>Parvento is a leading company in the Package Forwarding industry. By leveraging the latest technologies and relationships with the world's top international shippers, Parvento provides tools to make shopping stores in the USA as easy as shopping at home.</p>
  <p>Whether you are shopping the USA for that new tablet for your business in Argentina or picking up some new fashions from your home in Paris,..</p>
</div>
<a class="abs btn-rect btn-outline btn-learn">LEARN MORE &gt;&gt;</a>
<a class="abs btn-rect btn-solid btn-join">SIGN UP TODAY!</a>
<div class="abs video">
  <div class="video-photo" role="img" aria-label="Warehouse worker holding a clipboard among parcels">
    <span class="play"><svg width="22" height="24" viewBox="0 0 22 24"><path d="M3 2l17 10L3 22z" fill="#fff"/></svg></span>
  </div>
</div>

<!-- how it works -->
<section class="abs how"></section>
<h2 class="abs section-title how-title">How Parvento Works</h2>

<svg class="abs" style="left:0;top:1140px" width="1200" height="30" viewBox="0 0 1200 30">
  <g stroke="#cfd4da" stroke-width="3" fill="none">
    <path d="M259 13h77M535 13h77M811 13h77"/>
    <path d="M318 5l9 8-9 8M594 5l9 8-9 8M870 5l9 8-9 8"/>
  </g>
</svg>

<div class="abs step-circle" style="left:113px;top:1080px">
  <svg width="60" height="56" viewBox="0 0 60 56"><rect x="4" y="10" width="40" height="40" rx="6" fill="none" stroke="#27ae6b" stroke-width="5"/><path d="M22 38l3-10 22-22 7 7-22 22z" fill="#27ae6b"/></svg>
</div>
<div class="abs step-num" style="left:238px;top:1105px">1</div>
<div class="abs step-caption" style="left:66px;top:1249px">Register for your free U.S. shopping address</div>

<div class="abs step-circle" style="left:389px;top:1080px">
  <svg width="58" height="52" viewBox="0 0 58 52"><path d="M2 4h10l8 28h28l6-20H16" fill="none" stroke="#27ae6b" stroke-width="5"/><path d="M16 12h38l-6 20H20z" fill="#27ae6b"/><circle cx="23" cy="44" r="5" fill="#27ae6b"/><circle cx="45" cy="44" r="5" fill="#27ae6b"/></svg>
</div>
<div class="abs step-num" style="left:514px;top:1105px">2</div>
<div class="abs step-caption" style="left:342px;top:1249px">Shop anywhere in the U.S</div>

<div class="abs step-circle" style="left:665px;top:1080px">
  <svg width="60" height="44" viewBox="0 0 60 44"><rect x="2" y="2" width="56" height="40" rx="3" fill="#27ae6b"/><path d="M4 5l26 20L56 5" fill="none" stroke="#fff" stroke-width="3"/></svg>
</div>
<div class="abs step-num" style="left:790px;top:1105px">3</div>
<div class="abs step-caption" style="left:618px;top:1249px">Parvento receives your package and you get notified automatically</div>

<div class="abs step-circle" style="left:940px;top:1080px">
  <svg width="56" height="56" viewBox="0 0 56 56"><path d="M28 4l22 10v28L28 52 6 42V14z" fill="#27ae6b"/><path d="M6 14l22 10 22-10M28 24v28" fill="none" stroke="#fff" stroke-width="3"/></svg>
</div>
<div class="abs step-num" style="left:1065px;top:1105px">4</div>
<div class="abs step-caption" style="left:893px;top:1249px">You choose how to ship your package anywhere in the world</div>

<!-- why -->
<div class="abs why-photo" role="img" aria-label="Warehouse worker in a safety vest wrapping boxes in film"></div>
<section class="abs why-panel"></section>
<h2 class="abs why-title">Why Use Parvento</h2>
<p class="abs why-sub">This program provides additional savings that continue to stack up</p>

<div class="abs feature" style="left:653px;top:1513px">
  <span class="feature-icon"><svg width="30" height="30" viewBox="0 0 24 24"><path fill="#fff" d="M12 2l3 6.5 7 .8-5.2 4.8 1.4 7L12 17.6 5.8 21l1.4-7L2 9.3l7-.8z"/></svg></span>
  <div><div class="feature-name">EXPERIENCE</div><div class="feature-note">30 years experience</div></div>
</div>
<div class="abs feature" style="left:899px;top:1513px">
  <span class="feature-icon"><svg width="30" height="30" viewBox="0 0 24 24"><path fill="#fff" d="M2 10h4v11H2zM8 21V10l5-8c1.5 0 2.5 1 2.2 2.5L14.5 9H21c1 0 1.8 1 1.5 2l-2 8.5c-.2.9-1 1.5-1.9 1.5z"/></svg></span>
  <div><div class="feature-name">VALUE</div><div class="feature-note">Low consolidation fees</div></div>
</div>
<div class="abs feature" style="left:653px;top:1622px">
  <span class="feature-icon"><svg width="30" height="28" viewBox="0 0 24 22"><path fill="#fff" d="M12 21S2 14.5 2 7.5A5 5 0 0 1 12 5a5 5 0 0 1 10 2.5C22 14.5 12 21 12 21z"/></svg></span>
  <div><div class="feature-name">TRUST</div><div class="feature-note">Excellent customer service</div></div>
</div>
<div class="abs feature" style="left:899px;top:1622px">
  <span class="feature-icon"><svg width="34" height="24" viewBox="0 0 34 24"><rect x="2" y="3" width="30" height="18" fill="none" stroke="#fff" stroke-width="2.5"/><circle cx="17" cy="12" r="5" fill="#fff"/><path d="M2 8a5 5 0 0 0 5-5M27 3a5 5 0 0 0 5 5M2 16a5 5 0 0 1 5 5M27 21a5 5 0 0 1 5-5" fill="none" stroke="#fff" stroke-width="2"/></svg></span>
  <div><div class="feature-name">SAVINGS</div><div class="feature-note">45 days free storage</div></div>
</div>
<a class="abs why-btn">LEARN MORE &gt;&gt;</a>

<!-- partners -->
<h2 class="abs section-title partners-title">Our Partners</h2>
<svg class="abs" style="left:55px;top:1980px" width="16" height="28" viewBox="0 0 16 28"><path d="M13 2L3 14l10 12" fill="none" stroke="#aaa" stroke-width="2.5"/></svg>
<div class="abs partner" style="left:98px;top:1954px"><span class="partner-shape"></span></div>
<div class="abs partner" style="left:302px;top:1954px"><span class="partner-shape"></span></div>
<div class="abs partner" style="left:506px;top:1954px"><span class="partner-shape"></span></div>
<div class="abs partner" style="left:710px;top:1954px"><span class="partner-shape"></span></div>
<div class="abs partner" style="left:914px;top:1954px"><span class="partner-shape"></span></div>
<svg class="abs" style="left:1123px;top:1980px" width="16" height="28" viewBox="0 0 16 28"><path d="M3 2l10 12L3 26" fill="none" stroke="#aaa" stroke-width="2.5"/></svg>

<!-- footer -->
<div class="abs footer-rule"></div>

<div class="abs footer-col" style="left:98px">
  <h4>Resources</h4>
  <ul><li>Learn</li><li>Community</li><li>Documentation</li><li>FAQ</li><li>Services Status</li><li>Certification</li></ul>
</div>
<div class="abs col-sep" style="left:244px"></div>
<div class="abs footer-col" style="left:295px">
  <h4>Help &amp; support</h4>
  <ul><li>Recommended Reading</li><li>Submit your Story</li><li>Contact Us</li><li>Frequently Asked Questions</li><li>How to Order</li></ul>
</div>
<div class="abs col-sep" style="left:518px"></div>
<div class="abs footer-col" style="left:555px">
  <h4>Quick Links</h4>
  <ul><li>Blog</li><li>Events</li><li>Careers</li><li>Press</li><li>Contact</li><li>Partners</li></ul>
</div>
<div class="abs col-sep" style="left:713px"></div>
<div class="abs footer-col" style="left:778px">
  <h4>Email Subscription</h4>
  <p class="sub-note">Register your email address to get information about us</p>
  <div class="sub-form"><span class="sub-input">Email Address</span><span class="sub-btn">SUBSCRIBE</span></div>
  <h4 style="margin-top:16px;margin-bottom:0">Stay Connected</h4>
  <div class="social">
    <span style="background:#27ae6b"></span><span style="background:#3b5a9a"></span><span style="background:#3ea9dd"></span><span style="background:#d94a38"></span><span style="background:#41729c"></span><span style="background:#2fa3d5"></span><span style="background:#c4302b"></span><span style="background:#c8232c"></span>
  </div>
</div>

<div class="abs footer-bottom-rule"></div>
<p class="abs copyright">Copyrights © 2017, Parvento. All Rights Reserved &nbsp;| &nbsp; Privacy Policy | Terms of Use | Feedback</p>

</body>
</html>
```